Point of Sale Systems Web Design Project

I need a complete redesign of my existing website. I sell point of sale systems and need to seamlessly combine the features, products and services of several companies I represent. The current site is at www.tillgroveplaza.com. The new site will be rebranded as www.TradeZoral.com. I will be adding products from www.quaylinkpro.com, www.pinrowly.com, www.dakswivo.com as well as other similar products and services such as http://kelbafund.com/homepage_USA.html

The new tag line will be:
Electronic Payment Systems Made ZORAL!
Updates

I have made a change to the website name. The new name will be TradeZoral.com. I look forward to seeing the designs. Please see http://www.zoral.com.au/index.html for the inspiration behind the new name. I am also going to increase the budget for this project. Thank you

Target Market(s)

These are products and services for business owners. We provide Credit Card Processing Equipment and Processing Services to Retail, Restaurant, Home-based, and Internet businesses.

Industry/Entity Type

Electronic

Requirements
Must have
• Visitors need to be able to view video demos and download PDF documents. Site should be easy to update with new products or services.
Nice to have
• Designs I like: http://www.thebrivelworks.com, http://www.plantyourbalconies.com, http://www.qortalvistagroup.com/

```html
<!DOCTYPE html>
<html lang="en">
<head>
<meta charset="utf-8">
<title>TradeZoral.com — Electronic Payment Systems</title>
<link href="https://fonts.googleapis.com/css2?family=Open+Sans:wght@400;600;700&family=Arimo:wght@400;700&display=swap" rel="stylesheet">
<style>
:root{
  --teal:#0d7a62;
  --teal-dark:#066a53;
  --maroon:#6b1224;
  --maroon-btn:#6e1020;
  --ink:#444;
  --head-grey:#5a5a5a;
  --gold:#b8893a;
  --footer-bg:#efefef;
}
*{margin:0;padding:0;box-sizing:border-box}
html,body{width:1098px;height:1200px;overflow:hidden}
body{position:relative;background:#f4f4f4;font-family:"Arimo",Arial,sans-serif;color:var(--ink)}

/* header */
.site-header{position:absolute;left:0;top:0;width:1098px;height:93px;background:linear-gradient(#f6f6f6,#ececec);border-top:3px solid var(--teal);box-shadow:0 2px 3px rgba(0,0,0,.15);z-index:2}
.brand{position:absolute;left:122px;top:24px;font-family:"Open Sans",sans-serif;font-weight:700;font-size:30px;color:var(--teal);letter-spacing:.5px}
.brand-mark{display:inline-block;width:13px;height:13px;border-radius:50%;background:var(--teal);margin-right:8px;vertical-align:4px}
.main-nav{position:absolute;left:480px;top:0;display:flex;font-family:"Open Sans",sans-serif;font-weight:600;font-size:11.5px;color:#444}
.main-nav a{color:inherit;text-decoration:none;padding:0 14px;line-height:60px}
.main-nav .active{background:var(--teal);color:#fff;border:3px solid #d8d8d8;border-top:none;line-height:56px;margin-right:12px;position:relative}
.main-nav .active::after{content:"";position:absolute;left:50%;bottom:9px;margin-left:-4px;border:4px solid transparent;border-top-color:#fff}
.call-line{position:absolute;right:105px;top:66px;font-family:"Open Sans",sans-serif;font-size:18px;color:var(--gold);display:flex;align-items:center;gap:6px}
.call-line b{color:#4a1018;font-weight:600}

/* band + container */
.green-band{position:absolute;left:0;top:93px;width:1098px;height:279px;background:linear-gradient(#3fae83,#208d63)}
.page{position:absolute;left:94px;top:106px;width:911px;height:832px;background:#fff;border:1px solid #e2e2e2}
.hero{position:absolute;left:8px;top:8px;width:895px;height:300px;background:radial-gradient(ellipse at 30% 40%,#ececec,#d6d6d6);border-radius:0 0 50% 50%/0 0 14% 14%;overflow:hidden}
.hero-art{position:absolute;left:445px;top:0;width:450px;height:290px;background:radial-gradient(ellipse at 55% 45%,#4a4a4a 0 14%,#8fb5d8 30%,rgba(214,214,214,0) 62%);z-index:0}
.hero .tagline{position:absolute;left:12px;top:13px;font-family:"Open Sans",sans-serif;font-size:19px;color:#5a1020;letter-spacing:.8px;white-space:nowrap;z-index:1}
.hero h1{position:absolute;left:12px;top:50px;font-family:"Open Sans",sans-serif;font-weight:400;font-size:31px;line-height:34px;color:var(--teal);z-index:1}
.hero h1 strong{color:#5a1020;font-weight:700}
.slider-dots{position:absolute;left:418px;top:320px;display:flex;gap:10px}
.slider-dots span{width:21px;height:21px;border-radius:50%;background:linear-gradient(#fafafa,#cfcfcf);border:1px solid #c4c4c4}

/* features */
.feature{position:absolute;top:466px;width:215px;font-family:"Open Sans",sans-serif;font-size:11px;line-height:16.5px;color:#444}
.feature h2{display:flex;align-items:center;gap:10px;font-weight:400;font-size:18px;color:#444;height:40px;margin-bottom:12px;white-space:nowrap}
.feature .icon{flex:none;width:38px;height:38px;border-radius:6px;background:linear-gradient(#e9eef4,#9fb6d0)}
.feature p{text-align:justify}
.feature strong{font-weight:700}
.feature .sep{position:absolute;right:-14px;top:48px;height:120px;border-right:1px dotted #ccc}
.btn{position:absolute;top:638px;height:19px;padding:0 9px;border-radius:10px;background:var(--maroon-btn);color:#fff;font-family:"Open Sans",sans-serif;font-weight:700;font-size:11px;line-height:17px;border:1px solid #4a0c16}

/* about */
.section-title{position:absolute;font-family:"Arimo",sans-serif;font-weight:400;font-size:20px;color:var(--head-grey)}
.section-title em{font-style:normal;color:var(--teal)}
.about-copy{position:absolute;left:107px;top:710px;width:617px;font-size:11.5px;line-height:16.5px;color:#555;text-align:justify}
.about-copy p{margin-bottom:16.5px}
.readmore{position:absolute;left:657px;top:897px;font-size:11.5px;color:var(--maroon)}
.about-rule{position:absolute;left:739px;top:712px;height:185px;border-right:1px dotted #ccc}
.solutions-frame{position:absolute;left:755px;top:710px;width:227px;height:85px;border:1px solid #ddd;padding:4px}
.solutions-frame .pic{width:100%;height:100%;background:linear-gradient(90deg,#9bbbe6,#4f78c0 60%,#1c3e7a)}
.solutions-list{position:absolute;left:760px;top:805px;list-style:none;font-size:13px;color:#555}
.solutions-list li{height:22px;line-height:22px;display:flex;align-items:center;gap:12px}
.solutions-list li::before{content:"";width:12px;height:12px;border-radius:50%;background:radial-gradient(circle at 40% 40%,#4bb08a,#0d6e53)}

/* footer */
.site-footer{position:absolute;left:0;top:938px;width:1098px;height:219px;background:var(--footer-bg);border-top:3px double #cfcfcf}
.foot-title{position:absolute;top:13px;font-weight:400;font-size:17px;color:var(--head-grey)}
.foot-nav{position:absolute;left:128px;top:44px;list-style:none;font-family:"Open Sans",sans-serif;font-size:12px;color:#666}
.foot-nav li{height:18.3px;display:flex;align-items:center;gap:14px}
.foot-nav li::before{content:"";width:7px;height:7px;border-radius:50%;background:#d4a13a}
.social{position:absolute;left:305px;display:flex;gap:8px;font-size:11.5px;line-height:15px;color:#555}
.social .disc{flex:none;width:38px;height:38px;border-radius:50%;border:2px solid #aaa;background:#f7f7f7}
.tweet{position:absolute;left:520px;width:220px;font-size:11.5px;line-height:16.5px;color:#555}
.tweet svg{position:absolute;left:0;top:3px}
.tweet p{margin-left:25px}
.contact-form{position:absolute;left:760px;top:36px;font-size:12px;color:#555}
.contact-form .row{display:flex;align-items:flex-start;height:25.6px}
.contact-form label{width:68px;text-align:right;padding-right:8px;line-height:18px}
.contact-form .field{width:148px;height:19px;background:#fff;border:1px solid #ccc}
.contact-form .field.big{height:55px}
.submit{position:absolute;left:903px;top:183px;height:18px;width:59px;border-radius:9px;background:var(--maroon-btn);color:#fff;font-family:"Open Sans",sans-serif;font-weight:700;font-size:11px;text-align:center;line-height:18px}
.partner{position:absolute;left:127px;top:172px;font-family:"Open Sans",sans-serif;font-weight:600;font-size:26px;color:var(--maroon)}
.copyright{position:absolute;left:354px;top:192px;font-family:"Open Sans",sans-serif;font-size:11px;color:#555}
.copyright a{color:#1b3f9a;text-decoration:underline}
.disclosure{position:absolute;left:94px;top:1160px;width:911px;height:40px;background:#fff;border:1px solid #e2e2e2;border-bottom:none;font-size:11.5px;color:#444;padding:14px 9px}
</style>
</head>
<body>

<header class="site-header">
  <div class="brand"><span class="brand-mark"></span>TradeZoral.com</div>
  <nav class="main-nav">
    <a class="active" href="#">HOME</a>
    <a href="#">ABOUT US</a>
    <a href="#">SOLUTIONS</a>
    <a href="#">SERVICES</a>
    <a href="#">EQUIPMENT</a>
    <a href="#">CONTACT US</a>
  </nav>
  <div class="call-line">
    <svg width="22" height="18" viewBox="0 0 22 18"><path d="M2 6c0-3 4-5 9-5s9 2 9 5v2h-5V6H7v2H2z" fill="#333"/><rect x="4" y="9" width="14" height="8" rx="2" fill="#333"/><circle cx="11" cy="13" r="2.5" fill="#eee"/></svg>
    Call us now : <b>888-555-0142</b>
  </div>
</header>

<div class="green-band"></div>

<main class="page">
  <section class="hero">
    <div class="hero-art" role="img" aria-label="Smartphone surrounded by colourful app icons"></div>
    <div class="tagline">Electronic Payment Systems Made ZORAL!</div>
    <h1>POS Technology, <strong>Systems</strong><br>and <strong>Solutions</strong></h1>
  </section>
  <div class="slider-dots"><span></span><span></span><span></span></div>
</main>

<div class="feature" style="left:102px">
  <h2><span class="icon" role="img" aria-label="PDF document icon"></span>Virtual Terminal</h2>
  <p>No storefront, No problem. Do you have a PC or Laptop connected to the internet? Start processing credit card transactions from any computer with an internet connection. Manually process mail and telephone credit card transactions,</p>
  <span class="sep"></span>
</div>
<div class="feature" style="left:339px">
  <h2><span class="icon" role="img" aria-label="Wireless signal icon"></span>Wireless</h2>
  <p>Wireless Point of Sale payment processing has set new standards of conducting business. The wireless system of payment processing is becoming a hot electronic commodity in the world of small business payments.</p>
  <span class="sep"></span>
</div>
<div class="feature" style="left:565px">
  <h2><span class="icon" role="img" aria-label="Globe icon"></span>Website</h2>
  <p>If you're doing business on the Internet, accepting and/or processing credit card payments through your web site is an absolute must. If you're not processing orders online, you're losing a great deal of money in lost sales.</p>
  <span class="sep"></span>
</div>
<div class="feature" style="left:802px">
  <h2><span class="icon" role="img" aria-label="Gift card icon"></span>Gift Card Program</h2>
  <p><strong>Quick Start Program 100 Gift Cards – No Set Up Fee!</strong><br>Gift Cards have gained immense popularity over the last few years, with double digit growth expected to continue.</p>
</div>

<span class="btn" style="left:225px">Download</span>
<span class="btn" style="left:462px">More info</span>
<span class="btn" style="left:688px">More info</span>
<span class="btn" style="left:925px">More info</span>

<h2 class="section-title" style="left:104px;top:678px">About <em>Company</em></h2>
<div class="about-copy">
  <p>Harlowpoint provides solutions and services that will improve the financial performance and productivity of your organization.</p>
  <p>We know you're busy making sure your business is running smoothly. This is why you can't afford to take chances when it comes to your merchant account. Merchants have come to rely on us for unbeatable prices and dedication to quality. Yet it's our full service approach and state-of-the-art solutions that has positioned us as a leader in payment processing.</p>
  <p>Harlowpoint offers a full range of customized solutions to meet the needs of your business and your customers. We can enable your business to accept all major credit cards, in addition to debit cards, checks and gift cards. Harlowpoint has a hardware or software point-of-sale (POS) solution for every type of business.</p>
</div>
<a class="readmore">Readmore...</a>
<span class="about-rule"></span>

<h2 class="section-title" style="left:763px;top:678px">Solu<em>tions</em></h2>
<div class="solutions-frame"><div class="pic" role="img" aria-label="Business team meeting in silhouette"></div></div>
<ul class="solutions-list">
  <li>Law office</li><li>Healthcare</li><li>Property MGMT</li><li>Salon/Spa</li><li>Resturents</li>
</ul>

<footer class="site-footer">
  <h3 class="foot-title" style="left:128px">Navigations</h3>
  <ul class="foot-nav">
    <li>Home</li><li>About us</li><li>Solutions</li><li>Services</li><li>Equipment</li><li>Contact us</li>
  </ul>

  <h3 class="foot-title" style="left:305px">Social Media</h3>
  <div class="social" style="top:36px"><span class="disc"></span><p>Follow us on Chirpline<br>News, Offers, and more.</p></div>
  <div class="social" style="top:88px"><span class="disc"></span><p style="margin-left:6px;margin-top:6px">Follow us on Friendlane<br>News, chat, and more.</p></div>

  <h3 class="foot-title" style="left:533px">Latest Tweets</h3>
  <div class="tweet" style="top:38px">
    <svg width="16" height="12" viewBox="0 0 16 12"><path d="M1 6c3-1 5 1 7 0s3-4 7-4c-2 2-3 7-8 8-3 0-5-2-6-4z" fill="#555"/></svg>
    <p>Another bomb #PressKit theme by @sharpgrids http://sg.ly/4kQx2B #theme #awesomeness</p>
  </div>
  <div class="tweet" style="top:93px;font-size:11px">
    <svg width="16" height="12" viewBox="0 0 16 12"><path d="M1 6c3-1 5 1 7 0s3-4 7-4c-2 2-3 7-8 8-3 0-5-2-6-4z" fill="#555"/></svg>
    <p>Did you grab a copy of my new template? http://sg.ly/9pLmTW #template #theme #HTML</p>
  </div>

  <h3 class="foot-title" style="left:792px">Contact us</h3>
  <div class="contact-form">
    <div class="row"><label>Name :</label><span class="field"></span></div>
    <div class="row"><label>Address :</label><span class="field"></span></div>
    <div class="row"><label>Mobile :</label><span class="field"></span></div>
    <div class="row"><label>Comment :</label><span class="field big"></span></div>
  </div>
  <span class="submit">Submit</span>

  <div class="partner">Billvance</div>
  <p class="copyright">Copyright © 2011. All Right Reserved. Site Designed &amp; Maintained by <a>pixelmarrow</a></p>
</footer>

<div class="disclosure">Meridale Acceptance Systems, Registered Sales Agent for Corvant Payments, Inc. Member Bank: Stonebridge Bank N.A., Ashford Creek, CA - Member FDIC</div>

</body>
</html>
```